Orchard Vows Evening

We need a flyer we can post on Chatterloop announcing and event. It's a bridal fair for wedding vendors to showcase their services and talents at the Marvin T. Oakes Science Center, in Linden Park.

Date Thursday February 27, 2014
Time 6-9pm
Featuring a large selection of wedding vendors including complimentary bridal menu appetizers provided by the #1 Wedding Caterer in San Diego - The Maple Table Catering

Sponsored by

Marvin T Oakes Science Center &

The Maple Table Catering & Event Design Co,

Admission is Free for first 200 guests. After that admission is $20 per person

To RSVP or questions, please email OrchardVowsEvening@TheMapleTableCatering.example

Target Market(s)

Target demographic is 21-25 year old woman.

Industry/Entity Type

Wedding

Requirements
Must have
• one page. Two logos, one for Marvin T Oakes Science Center and the other for The Maple Table Catering.
• Needs to be sophisticated, fun, and appealing to newly engaged brides.
Nice to have
• Should have images that go with Science, Love, Bridal Fair and Weddings.

```html
<!DOCTYPE html>
<html lang="en">
<head>
<meta charset="utf-8">
<title>Orchard Vows Evening – Bridal Fair</title>
<link rel="stylesheet" href="https://fonts.googleapis.com/css2?family=Great+Vibes&family=Montserrat:wght@500;700&family=Oswald:wght@300;400;500;600&display=swap">
<style>
  :root {
    --teal: #17a396;
    --teal-deep: #128b80;
    --field: #e3f1f0;
    --red: #b3232f;
    --pink: #f6c3c1;
    --pink-soft: #fbdcdb;
    --white: #ffffff;
  }
  * { margin: 0; padding: 0; box-sizing: border-box; }
  html, body { width: 1006px; height: 1200px; overflow: hidden; background: #f2f2f2; }
  .flyer {
    position: relative; width: 1006px; height: 1200px;
    background: var(--teal); padding: 28px;
  }
  .field {
    position: relative; width: 100%; height: 100%;
    background: var(--field); overflow: hidden;
  }
  .abs { position: absolute; }

  .big-heart { left: 170px; top: 18px; width: 360px; height: 420px; }
  .title { left: 170px; top: 140px; width: 360px; text-align: center; color: var(--white); }
  .title-caps { font-family: "Montserrat", sans-serif; font-weight: 500; font-size: 38px; letter-spacing: 1px; line-height: 1.1; }
  .title-script { font-family: "Great Vibes", cursive; font-size: 74px; line-height: 1; margin-top: 2px; }

  .mini-heart { fill: #c83b45; }

  .flask-art {
    left: 100px; top: 660px; width: 280px; height: 456px;
    background: linear-gradient(180deg, var(--pink-soft) 0%, var(--pink) 40%, #3fb3a7 60%, var(--teal) 100%);
    border-radius: 14px; opacity: .9;
  }

  .event-title { left: 350px; top: 476px; width: 560px; text-align: center;
    font-family: "Great Vibes", cursive; font-size: 96px; font-weight: 400; color: var(--red); line-height: 1; }
  .rule { height: 3px; background: var(--red); }
  .rule-top { left: 362px; top: 600px; width: 548px; }
  .rule-mid { left: 362px; top: 700px; width: 548px; }

  .day { left: 362px; top: 606px; width: 262px; font-family: "Oswald", sans-serif; color: var(--teal); text-align: center; }
  .day-name { font-weight: 300; font-size: 52px; line-height: 1; letter-spacing: 1px; }
  .day-time { font-weight: 500; font-size: 28px; line-height: 1; color: var(--teal-deep); letter-spacing: 1px; }
  .divider { left: 630px; top: 612px; width: 3px; height: 80px; background: var(--red); }
  .date { left: 642px; top: 606px; font-family: "Oswald", sans-serif; color: var(--teal); }
  .date-month { font-weight: 400; font-size: 44px; line-height: 1; }
  .date-year { font-weight: 500; font-size: 36px; line-height: 1; letter-spacing: 3px; color: var(--teal-deep); }
  .date-day { left: 818px; top: 598px; font-family: "Oswald", sans-serif; font-weight: 300; font-size: 96px; line-height: 1; color: var(--teal); }

  .venue { left: 362px; top: 708px; width: 548px; text-align: center; font-family: "Oswald", sans-serif; color: var(--red); }
  .venue-name { font-weight: 400; font-size: 35px; line-height: 1.1; }
  .venue-park { font-weight: 600; font-size: 46px; letter-spacing: 9px; line-height: 1.1; }

  .ribbon { left: 348px; top: 804px; width: 576px; height: 86px; }
  .ribbon-text { left: 398px; top: 814px; width: 476px; text-align: center;
    font-family: "Oswald", sans-serif; font-weight: 500; font-size: 17px; line-height: 22px;
    color: var(--teal-deep); text-transform: uppercase; letter-spacing: .5px; }

  .caterer { left: 360px; top: 894px; width: 560px; height: 50px; }
  .caterer-name { left: 360px; top: 894px; width: 560px; text-align: center;
    font-family: "Great Vibes", cursive; font-size: 34px; color: var(--red); line-height: 48px; }

  .price-heart { width: 84px; height: 78px; }
  .price-label { font-family: "Oswald", sans-serif; font-weight: 600; font-size: 24px; color: var(--red); text-align: center; width: 84px; line-height: 1; }
  .price-note { font-family: "Oswald", sans-serif; font-weight: 500; font-size: 17px; color: var(--teal-deep); text-transform: uppercase; line-height: 1.15; }

  .sponsor-label { left: 410px; top: 1044px; width: 110px; text-align: center; font-family: "Oswald", sans-serif; font-weight: 500; font-size: 20px; line-height: 1.1; color: var(--red); letter-spacing: 1px; }
  .brace { font-family: "Oswald", sans-serif; font-weight: 300; font-size: 86px; line-height: 1; color: var(--red); }
  .sponsor { font-family: "Great Vibes", cursive; line-height: 1.05; color: var(--teal-deep); }
  .sponsor-science { left: 546px; top: 1046px; font-size: 23px; }
  .sponsor-caterer { left: 748px; top: 1032px; font-size: 20px; line-height: 1; }
  .amp { left: 700px; top: 1050px; width: 40px; height: 40px; border-radius: 50%; background: var(--red); color: var(--white);
    font-family: "Montserrat", sans-serif; font-weight: 700; font-size: 22px; text-align: center; line-height: 40px; }

  .rsvp { left: 350px; top: 1100px; width: 590px; text-align: center; font-family: "Oswald", sans-serif; font-weight: 500; font-size: 18px; line-height: 26px; color: var(--teal-deep); text-transform: uppercase; }
  .rsvp-label { color: var(--red); font-weight: 600; font-size: 23px; margin-right: 6px; }
</style>
</head>
<body>
<main class="flyer">
  <div class="field">

    <svg class="abs big-heart" viewBox="0 0 100 100" aria-hidden="true">
      <path d="M50 96 C40 84 4 60 4 30 C4 12 18 2 31 2 C41 2 47 8 50 16 C53 8 59 2 69 2 C82 2 96 12 96 30 C96 60 60 84 50 96 Z" fill="#c2313c"/>
    </svg>
    <div class="abs title">
      <div class="title-caps">ORCHARD<br>VOWS</div>
      <div class="title-script">Evening</div>
    </div>

    <svg class="abs" style="left:120px;top:320px;width:260px;height:330px" viewBox="0 0 260 330" aria-hidden="true">
      <defs><path id="h" d="M0 -6 C-4 -14 -16 -14 -16 -3 C-16 6 -4 12 0 18 C4 12 16 6 16 -3 C16 -14 4 -14 0 -6 Z"/></defs>
      <use href="#h" class="mini-heart" transform="translate(30 30) scale(1.5)"/>
      <use href="#h" class="mini-heart" transform="translate(100 100) scale(1.9)"/>
      <use href="#h" class="mini-heart" transform="translate(28 150) scale(1.3)"/>
      <use href="#h" class="mini-heart" transform="translate(130 180) scale(1.5)"/>
      <use href="#h" class="mini-heart" transform="translate(60 220) scale(0.9)"/>
      <use href="#h" class="mini-heart" transform="translate(110 250) scale(1.1)"/>
      <use href="#h" class="mini-heart" transform="translate(92 300) scale(0.8)"/>
    </svg>

    <div class="abs flask-art" role="img" aria-label="Illustration of a pink laboratory flask filled with teal liquid and floating hearts"></div>

    <h1 class="abs event-title">Bridal Fair</h1>
    <div class="abs rule rule-top"></div>
    <div class="abs day">
      <div class="day-name">THURSDAY</div>
      <div class="day-time">6 PM - 9 PM</div>
    </div>
    <div class="abs divider"></div>
    <div class="abs date">
      <div class="date-month">FEBRUARY</div>
      <div class="date-year">2014</div>
    </div>
    <div class="abs date-day">27</div>
    <div class="abs rule rule-mid"></div>

    <div class="abs venue">
      <div class="venue-name">MARVIN T. OAKES SCIENCE CENTER</div>
      <div class="venue-park">LINDEN PARK</div>
    </div>

    <svg class="abs ribbon" viewBox="0 0 576 86" aria-hidden="true">
      <polygon points="0,6 576,6 548,43 576,80 0,80 28,43" fill="var(--pink-soft)" stroke="var(--pink)" stroke-width="3"/>
    </svg>
    <div class="abs ribbon-text">
      Featuring a large selection of wedding vendors<br>
      including complimentary bridal menu appetizers<br>
      provided by the #1 wedding caterer in San Diego
    </div>

    <svg class="abs caterer" viewBox="0 0 560 50" aria-hidden="true">
      <g stroke="var(--red)" stroke-width="2" fill="var(--red)">
        <line x1="10" y1="28" x2="86" y2="28"/><polygon points="86,23 96,28 86,33"/>
        <line x1="474" y1="28" x2="550" y2="28"/><polygon points="474,23 464,28 474,33"/>
      </g>
    </svg>
    <div class="abs caterer-name">The Maple Table Catering</div>

    <svg class="abs price-heart" style="left:460px;top:948px" viewBox="0 0 100 92" aria-hidden="true">
      <path d="M50 90 C38 78 2 56 2 28 C2 12 14 2 28 2 C38 2 46 8 50 16 C54 8 62 2 72 2 C86 2 98 12 98 28 C98 56 62 78 50 90 Z" fill="var(--pink)"/>
    </svg>
    <div class="abs price-label" style="left:460px;top:974px">FREE</div>
    <div class="abs price-note" style="left:556px;top:962px">Admission for<br>first 200 guests</div>

    <svg class="abs price-heart" style="left:690px;top:948px" viewBox="0 0 100 92" aria-hidden="true">
      <path d="M50 90 C38 78 2 56 2 28 C2 12 14 2 28 2 C38 2 46 8 50 16 C54 8 62 2 72 2 C86 2 98 12 98 28 C98 56 62 78 50 90 Z" fill="var(--pink)"/>
    </svg>
    <div class="abs price-label" style="left:690px;top:974px">$20</div>
    <div class="abs price-note" style="left:786px;top:962px">Per person<br>after that</div>

    <div class="abs sponsor-label">SPONSORED<br>BY</div>
    <div class="abs brace" style="left:522px;top:1024px">{</div>
    <div class="abs sponsor sponsor-science">Marvin T Oakes<br>Science Center</div>
    <div class="abs amp">&amp;</div>
    <div class="abs sponsor sponsor-caterer">The Maple Table<br>Catering &amp; Event<br>Design Co.</div>
    <div class="abs brace" style="left:904px;top:1024px">}</div>

    <div class="abs rsvp"><span class="rsvp-label">RSVP</span>OrchardVowsEvening@TheMapleTableCatering.example</div>
  </div>
</main>
</body>
</html>
```